Sedona Themed Wedding Invitation & RSVP

*We have added our "Save the Date" for reference. We are not looking for an exact match, but we'd like the invitation and the "Save the Date" to coordinate. Our wedding colors are light pink, light green, cream, and gold. We have also added pictures of bouquets to give you an idea of the color palette and also examples of flowers and greenery to use in the invitation. What we like about the "Save the Date" is that it draws on the wedding colors and brings them in through the colors of the sunset.
*We have also added additional pictures the venue, the Le Verger Lodge, and several maps. We hope that you can use these to get a better feel for our venue and the theme of our wedding. It will be soft and romantic and at the very height of spring.
* We appreciated that many designers incorporated the Lodge at Le Vergre, we'd like to see more of that.
*Please note that we included some photos of Sedona for inspiration, please do not feel tied to these, do your own research and find what works best with your design.
*These maps are being included as references, but they are the work of other artists. Please make your own map from scratch and use these as references.
We would like a vertical quad-fold wedding invitation that has a perforated edge RSVP which can be sent as a postcard.
We have attached pictures of a similar style of invitation to serve as an example of the overall style we are looking for. We would like to see the end project be in a similar style of watercolor, but it would be Sedona themed throughout (rather than the forest theme presented in the attached example). We have also attached pictures of Sedona to serve as further inspiration. Below, we have provided an outline organized by panel (four panels on the front and four panels on the back) with descriptions of the more specific details:
-Front four panels:
-Panel 1: "Please join us for the wedding of Tobias and Colette"
-Panel 2: "Come out and celebrate. [INSERT TIME OF WEDDING HERE]
Saturday, May First 2021 at Le Verger de Rimoux"
-Panel 3: Custom map of Sedona. Include Le Verger de Rimoux on the
map (exemplar picture is of an idea for this is also included below)
- Panel 4: RSVP similar to one in the exemplar invitation. For RSVP date
deadline use April 1st, 2021. Address is 2287 W Marlow St Phoenix, AZ
85019
-Back four panels:
-Panel 1: Venue: Le Verger de Rimoux. 418 Fennick Ln, Sedona, AZ 86339.
Please arrive no earlier than XXX PM when valet services begin. Dinner
and dancing to follow the ceremony
-Panel 2: Hotels: Le Verger de Rimoux 418 Fennick Ln, Sedona, AZ 86339
(800) 612-3908; Bramwell Inn 917 N Tolliver Rd, Sedona, AZ 86339
(855) 238-6041.
"Hotel reservations can also be made through the links provided on our
website"
- Panel 3: "We have reserved a block of rooms for our guests. Please
mention the Pruett Halloway Wedding when you call to reserve."
"For additional details, please visit our wedding website and take a walk
down memory lane with us as we prepare to celebrate the rest of our
lives together: [INSERT WEDDING WEBSITE HERE AND
PASSWORD]"
- Panel 4: "Ceremony and celebration will be outdoors. Semi-formal attire
and flat shoes are recommended."
"Additionally, although we love your children, we want our wedding to
be your night off! Please know space is very limited; accordingly, we
encourage a weekend getaway for the grownups."
We'd like to have a succulent and rose at the bottom of the panel (an
exemplar picture is of an idea for this is also included below)
Updates
We have given extensive feedback to designers and would like to give them time to adjust their designs. Additionally, we have incorporated a lot more images into the brief that we hope will help!

```html
<!DOCTYPE html>
<html lang="en">
<head>
<meta charset="utf-8">
<title>Venue &amp; Hotels – Pruett Halloway Wedding</title>
<link href="https://fonts.googleapis.com/css2?family=Amatic+SC:wght@400;700&family=Kaushan+Script&family=Dancing+Script:wght@600&display=swap" rel="stylesheet">
<style>
  :root {
    --ink: #4a1d10;
    --blush: #f3a7ae;
    --cream: #f8f5ef;
    --paper: #fcf6f2;
    --mist: #e7e4dc;
    --sky: #c8ecef;
    --rock-top: #9a6a45;
    --rock-bottom: #b86a32;
    --succulent: #9fcfae;
    --white: #ffffff;
  }
  * { box-sizing: border-box; margin: 0; padding: 0; }
  html, body { width: 1200px; height: 3200px; overflow: hidden; }
  body { background: var(--cream); color: var(--ink); font-family: "Amatic SC", sans-serif; }
  .sheet { position: relative; width: 1200px; height: 3200px; }
  .panel { position: absolute; left: 0; width: 1200px; overflow: hidden; }
  .panel--venue { top: 0; height: 801px; background: radial-gradient(ellipse at 40% 30%, #fbfaf6, var(--cream) 70%, #efece4); }
  .panel--hotels { top: 801px; height: 798px; background: var(--sky); }
  .panel--details { top: 1599px; height: 798px; background: linear-gradient(180deg, var(--paper), #faf3ee); }
  .panel--family { top: 2397px; height: 803px; background: radial-gradient(ellipse at 50% 40%, #f3f1ec, var(--mist) 80%); }

  .panel-title { position: absolute; font-family: "Kaushan Script", cursive; color: var(--blush); line-height: 1; }
  .panel--venue .panel-title { left: -6px; top: 10px; font-size: 230px; }
  .panel--hotels .panel-title { left: -4px; top: 10px; font-size: 220px; z-index: 2; }

  .centered { position: absolute; left: 0; width: 100%; text-align: center; }
  .venue-name { top: 340px; font-size: 84px; font-weight: 700; letter-spacing: 1px; }
  .venue-address { top: 430px; font-family: "Dancing Script", cursive; font-size: 50px; }
  .notice { font-size: 56px; font-weight: 700; line-height: 68px; }
  .panel--venue .notice { top: 575px; }

  .succulent-art { position: absolute; right: 0; top: 225px; width: 500px; height: 576px;
    background: radial-gradient(ellipse at 70% 70%, var(--succulent), rgba(159,207,174,0.35) 55%, rgba(159,207,174,0) 75%); }

  .landscape-art { position: absolute; left: 0; top: 235px; width: 1200px; height: 563px;
    background: linear-gradient(180deg, var(--rock-top), var(--rock-bottom) 60%, #7a4a2a); }
  .hotel-col { position: absolute; top: 375px; width: 560px; text-align: center; color: var(--white); z-index: 2; }
  .hotel-col--left { left: 20px; }
  .hotel-col--right { left: 590px; }
  .hotel-name { font-size: 76px; font-weight: 400; line-height: 1; }
  .hotel-address { font-family: "Dancing Script", cursive; font-size: 36px; margin-top: 18px; }
  .hotel-phone { font-family: "Dancing Script", cursive; font-size: 34px; margin-top: 16px; }
  .hotel-note { top: 630px; color: var(--white); font-size: 52px; font-weight: 700; line-height: 68px; z-index: 2; }

  .quote { font-size: 62px; font-weight: 400; line-height: 68px; letter-spacing: 1px; }
  .quote--rooms { top: 85px; }
  .quote--website { top: 335px; }
  .website { top: 612px; font-family: "Dancing Script", cursive; font-size: 50px; }

  .panel--family .quote { top: 105px; font-weight: 700; font-size: 60px; }
  .garland-art { position: absolute; left: 143px; top: 410px; width: 894px; height: 311px;
    background: radial-gradient(ellipse at 50% 50%, #8fc4a0 0%, #f3aaa8 35%, rgba(243,170,168,0.4) 60%, rgba(231,228,220,0) 75%); }
</style>
</head>
<body>
<main class="sheet">
  <section class="panel panel--venue">
    <h1 class="panel-title">Venue</h1>
    <div class="succulent-art" role="img" aria-label="Watercolor succulents and lavender sprigs"></div>
    <h2 class="centered venue-name">LE VERGER DE RIMOUX</h2>
    <p class="centered venue-address">418 Fennick Ln, Sedona, AZ 86339</p>
    <p class="centered notice">Please arrive no earlier than XXX PM when valet services begin.<br>Dinner and dancing to follow the ceremony</p>
  </section>

  <section class="panel panel--hotels">
    <div class="landscape-art" role="img" aria-label="Watercolor painting of Sedona red rock mountains above the lodge"></div>
    <h1 class="panel-title">Hotels</h1>
    <div class="hotel-col hotel-col--left">
      <h3 class="hotel-name">Le Verger de Rimoux</h3>
      <p class="hotel-address">418 Fennick Ln, Sedona, AZ 86339</p>
      <p class="hotel-phone">(800) 612-3908</p>
    </div>
    <div class="hotel-col hotel-col--right">
      <h3 class="hotel-name">Bramwell Inn</h3>
      <p class="hotel-address">917 N Tolliver Rd, Sedona, AZ 86339</p>
      <p class="hotel-phone">(855) 238-6041.</p>
    </div>
    <p class="centered hotel-note">"Hotel reservations can also be made through the links<br>provided on our website"</p>
  </section>

  <section class="panel panel--details">
    <p class="centered quote quote--rooms">"We have reserved a block of rooms for our guests.<br>Please mention the Pruett Halloway Wedding<br>when you call to reserve."</p>
    <p class="centered quote quote--website">"For additional details, please visit our wedding website<br>and take a walk down memory lane with us<br>as we prepare to celebrate the rest of our lives together:</p>
    <p class="centered website">[Insert weddng website here and password]"</p>
  </section>

  <section class="panel panel--family">
    <p class="centered quote">"Additionally, although we love your children,<br>we want our wedding to be your night off!<br>Please know space is very limited; accordingly,<br>we encourage a weekend getaway for the grownups."</p>
    <div class="garland-art" role="img" aria-label="Watercolor garland of pink roses around a green succulent"></div>
  </section>
</main>
</body>
</html>
```